Restaurant website built on Plinko’s responsive platform- No coding skills needed

We are looking to add to our company's website www.plinkoweb.example a new inspiration page that will include examples of sites built using Plinko's platform.
In order to make it relevant, we would like to have multiple choices for every category, one of the categories is “restaurants.”

REQUIREMENTS:
o Build a "fake" restaurant site on Plinko’s responsive platform, no real restaurant information is needed. The site will include:
1. Homepage
• Restaurant header (no logo)
• Paragraph about the restaurant (can be Lorem ipsum)
• Contact details and contact buttons
• Gribbo reviews
• Reserve-a-table widget
• Open hours
2. Menu page
• You can use any menu you'd like
• Reserve a table widget
• Photo gallery
3. Footer
• Social Media links
• Map with location of restaurant

* Order of the elements is up to the designer
* Designer may add more elements as they see fit
* Designer may alter elements from page to page
* Designer will define the site color pallet and text style

****Learn more on how to create a website on Plinko's platform here
https://clipvault.example/584736201

INSTRUCTIONS FOR THIS PROJECT:
Register for a 30-day free trial for Pro access to the platform:
http://www.plinkoweb.example/plinkopro?_dm_referral=ArtHvn

a. After registering, access the dashboard and click on “Create Responsive Website.”
b. Choose a template
c. Start editing! .
d. No need to publish. When ready, take a screenshot of the preview and submit the screenshot to this ArtHaven project. Include the URL/Link to the preview within the submission description.
e. For more information on Plinko, visit the support page at https://support.plinkoweb.example/02PlinkoOne/Quick_Guide OR call our Support line Mon.-Fri., 9AM-9PM ET.1-866-555-0147

DESIGN PREFERENCES
freestyle (not related to the Plinko brand)

DESIGN SAMPLES (for inspiration)
http://www.plinkoweb.example/responsive-website/templates

What not to include in the design -
no restrictions

DELIVERABLES:
* Website on Plinko (No PSD. No coding needed)
* Screenshot preview to ArtHaven with URL/link to your site’s preview.

ABOUT THE COMPANY:
Plinko is a website builder based in California that allow designers, web designers and practically anyone to build its own site. No development and/or technical skills required.

NOTE:
* Plinko is an external site and is not part of ArtHaven
* Please refer to Plinko's Terms and Conditions for information regarding how submissions will be handled (http://www.plinkoweb.example/legal/terms)

Target Market(s)

SMBs and web designers that want to create simple, professional and beautiful websites

Industry/Entity Type

Restaurant

Number of Pages Required

2 page

Requirements
Must have
• Please send a preview of the site you created on Plinko, NOT a PSD/JPEG
Should not have
• No coding skills are needed- any web designer can build a site on Plinko

```html
<!DOCTYPE html>
<html lang="en">
<head>
<meta charset="utf-8">
<title>The Fern Restaurant</title>
<link rel="stylesheet" href="https://fonts.googleapis.com/css2?family=Carlito:ital,wght@0,400;0,700;1,400&family=Open+Sans:wght@400;600&display=swap">
<style>
  :root {
    --ink: #0d0d0d;
    --paper: #ffffff;
    --accent: #e8121b;
    --accent-dark: #9c1420;
    --nav-grey: #7a7a7a;
    --rule: #d8d8d8;
    --body-text: #3a3a3a;
    --field-line: #c9c9c9;
    --social: #6b6b6b;
    --photo-warm: #d2521f;
    --photo-deep: #7a2410;
    --photo-green: #a9d65a;
  }
  * { box-sizing: border-box; margin: 0; padding: 0; }
  html, body { width: 1200px; height: 814px; overflow: hidden; background: var(--paper); }
  .page { position: relative; width: 1200px; height: 814px; overflow: hidden; font-family: "Open Sans", sans-serif; }

  .main-nav { position: absolute; top: 14px; left: 182px; display: flex; height: 30px; align-items: center; }
  .main-nav a {
    font-family: "Carlito", sans-serif; font-style: italic; font-size: 15.5px;
    color: var(--nav-grey); text-decoration: none; padding: 0 15px; line-height: 30px;
    border-left: 1px solid #e4e4e4;
  }
  .main-nav a:first-child { border-left: none; color: var(--ink); }
  .main-nav a.is-current { color: var(--accent-dark); }

  .hero-art { position: absolute; top: 0; left: 0; }
  .brand-name {
    position: absolute; top: 100px; left: 528px; width: 200px; text-align: center;
    font-family: "Carlito", sans-serif; font-size: 29px; letter-spacing: 1.5px; color: var(--paper);
  }
  .slider-dots { position: absolute; top: 200px; left: 551px; display: flex; gap: 5px; }
  .slider-dots span { width: 20px; height: 20px; border-radius: 50%; background: var(--paper); }
  .slider-dots span.is-active { background: var(--accent); }

  .card { position: absolute; top: 354px; width: 279px; height: 294px; }
  .card-head { position: absolute; top: 0; left: 0; }
  .card-title {
    position: absolute; top: 52px; left: 0; width: 100%; text-align: center;
    font-family: "Carlito", sans-serif; font-size: 20px; color: var(--paper);
  }
  .card-body {
    position: absolute; top: 82px; left: 0; width: 100%; height: 212px;
    background: var(--paper); border: 1px solid var(--rule); border-top: none;
    padding: 14px 16px 0 17px; font-size: 8.1px; line-height: 12.2px; color: var(--body-text);
  }
  .card-body p + p { margin-top: 12px; }
  .card-about { left: 172px; }
  .card-reserve { left: 461px; }
  .card-reviews { left: 750px; }

  .reserve-form { padding-top: 16px; }
  .reserve-form label { display: block; font-size: 8.6px; font-weight: 600; letter-spacing: .3px; color: var(--ink); }
  .field { height: 25px; border: 1px solid var(--field-line); background: var(--paper); }
  .field-wide { margin-top: 4px; width: 246px; margin-bottom: 7px; }
  .form-row { display: flex; align-items: center; justify-content: space-between; width: 246px; margin-bottom: 8px; }
  .form-row .field { width: 178px; }
  .reserve-button {
    display: block; margin-left: 68px; width: 178px; height: 24px; border: none;
    background: var(--accent); color: var(--paper);
    font-family: "Carlito", sans-serif; font-style: italic; font-size: 15px;
  }

  .site-footer { position: absolute; left: 0; top: 0; width: 1200px; height: 814px; pointer-events: none; }
  .open-hours { position: absolute; top: 703px; left: 533px; width: 200px; text-align: center; font-family: "Carlito", sans-serif; font-size: 19.5px; color: var(--paper); }
  .bulb { position: absolute; top: 681px; left: 621px; }
  .social-links { position: absolute; top: 752px; left: 534px; display: flex; gap: 6px; }
  .social-links a { width: 27px; height: 27px; border-radius: 50%; background: var(--social); display: block; }
  .footer-links { position: absolute; top: 784px; left: 0; width: 1254px; text-align: center; font-size: 8.2px; color: var(--paper); }
  .copyright { position: absolute; top: 797px; left: 0; width: 1254px; text-align: center; font-size: 8.2px; color: var(--paper); }
</style>
</head>
<body>
<div class="page">

  <svg class="hero-art" width="1200" height="814" viewBox="0 0 1200 814">
    <defs>
      <clipPath id="hero-clip"><path d="M0 133 L628 61 L1200 100 L1200 680 L0 680 Z"/></clipPath>
      <linearGradient id="hero-base" x1="0" y1="0" x2="1" y2="0.4">
        <stop offset="0" stop-color="#8a3a18"/>
        <stop offset="0.35" stop-color="#c9601e"/>
        <stop offset="0.7" stop-color="#d4441a"/>
        <stop offset="1" stop-color="#a82c12"/>
      </linearGradient>
      <radialGradient id="hero-green" cx="0.25" cy="0.35" r="0.3">
        <stop offset="0" stop-color="#b7e06a" stop-opacity=".85"/>
        <stop offset="1" stop-color="#b7e06a" stop-opacity="0"/>
      </radialGradient>
      <radialGradient id="hero-glow" cx="0.75" cy="0.25" r="0.35">
        <stop offset="0" stop-color="#f08a3a" stop-opacity=".8"/>
        <stop offset="1" stop-color="#f08a3a" stop-opacity="0"/>
      </radialGradient>
      <linearGradient id="hero-fade" x1="0" y1="0" x2="0" y2="1">
        <stop offset="0.72" stop-color="#fff" stop-opacity="0"/>
        <stop offset="1" stop-color="#fff" stop-opacity=".95"/>
      </linearGradient>
    </defs>
    <g clip-path="url(#hero-clip)">
      <g role="img" aria-label="Close-up photo of a dish with celery sticks and red sauce on a warm blurred background">
        <rect x="0" y="0" width="1200" height="690" fill="url(#hero-base)"/>
        <rect x="0" y="0" width="1200" height="690" fill="url(#hero-glow)"/>
        <rect x="0" y="0" width="1200" height="690" fill="url(#hero-green)"/>
        <rect x="0" y="0" width="1200" height="690" fill="url(#hero-fade)"/>
      </g>
      <circle cx="628" cy="60" r="128" fill="var(--ink)"/>
    </g>
    <path d="M0 674 L522 730 A131.5 131.5 0 0 1 744 730 L1200 674 L1200 814 L0 814 Z" fill="var(--ink)"/>
  </svg>

  <nav class="main-nav">
    <a href="#">home</a>
    <a href="#">about us</a>
    <a href="#" class="is-current">Reserve-a-table</a>
    <a href="#">reviews</a>
    <a href="#">Menu</a>
    <a href="#">Photo gallery</a>
    <a href="#">Follow us</a>
    <a href="#">Sitemap</a>
    <a href="#">Contact us</a>
  </nav>

  <div class="brand-name">LOGO</div>
  <div class="slider-dots"><span></span><span></span><span></span><span></span><span class="is-active"></span></div>

  <section class="card card-about">
    <svg class="card-head" width="279" height="83" viewBox="0 0 279 83"><path d="M0 45 L279 0 L279 83 L0 83 Z" fill="var(--ink)"/></svg>
    <h2 class="card-title">about us</h2>
    <div class="card-body">
      <p>Lorem Ipsum is simply dummy text of the printing and typesetting industry. Lorem Ipsum has been the industry's standard dummy text ever since the 1500s, when an unknown printer took a galley of type and scrambled it to make a type specimen book.</p>
      <p>It has survived not only five centuries, but also the leap into electronic typesetting, remaining essentially unchanged. It was popularised in the 1960s with the release of Letraset sheets containing Lorem Ipsum passages, and more recently with desktop publishing software like Aldus PageMaker including versions of Lorem Ipsum.</p>
    </div>
  </section>

  <section class="card card-reserve">
    <svg class="card-head" width="279" height="83" viewBox="0 0 279 83"><path d="M0 45 L279 0 L279 83 L0 83 Z" fill="var(--ink)"/></svg>
    <h2 class="card-title">Reserve-a-table</h2>
    <form class="card-body reserve-form">
      <label>CHOOSE YOUR LOCATION</label>
      <div class="field field-wide"></div>
      <div class="form-row"><label>WHEN</label><div class="field"></div></div>
      <div class="form-row"><label>WHAT TIME</label><div class="field"></div></div>
      <div class="form-row"><label>NO. IN PARTY</label><div class="field"></div></div>
      <button type="button" class="reserve-button">reserve a table</button>
    </form>
  </section>

  <section class="card card-reviews">
    <svg class="card-head" width="279" height="83" viewBox="0 0 279 83"><path d="M0 45 L279 0 L279 83 L0 83 Z" fill="var(--ink)"/></svg>
    <h2 class="card-title">reviews</h2>
    <div class="card-body">
      <p>"Lorem Ipsum is simply dummy text of the printing and typesetting industry. Lorem Ipsum has been the industry's standard dummy text ever since the 1500s, when an unknown printer took a galley of type and scrambled it to make a type specimen book."</p>
      <p>"Lorem Ipsum is simply dummy text of the printing and typesetting industry. Lorem Ipsum has been the industry's standard dummy text ever since the 1500s, when an unknown printer took a galley of type and scrambled it to make a type specimen book."</p>
    </div>
  </section>

  <footer class="site-footer">
    <svg class="bulb" width="20" height="22" viewBox="0 0 20 22" fill="none" stroke="#fff" stroke-width="1.3">
      <path d="M10 1 A7 7 0 0 0 5.5 13.4 L6.5 16 L13.5 16 L14.5 13.4 A7 7 0 0 0 10 1 Z"/>
      <path d="M7 18 L13 18 M8 20.5 L12 20.5 M10 16 L10 9"/>
    </svg>
    <div class="open-hours">Open hours</div>
    <nav class="social-links" aria-label="Social media">
      <a href="#" aria-label="Social link 1"></a>
      <a href="#" aria-label="Social link 2"></a>
      <a href="#" aria-label="Social link 3"></a>
      <a href="#" aria-label="Social link 4"></a>
      <a href="#" aria-label="Social link 5"></a>
      <a href="#" aria-label="Social link 6"></a>
    </nav>
    <p class="footer-links">Press Room Reservations Menus Private Dining Specials &amp; Events 412 Club Contact Us Careers Diversity</p>
    <p class="copyright">Copyright 2010 The Fern Restaurant Privacy Policy</p>
  </footer>

</div>
</body>
</html>
```